Business Card Design - Photographer

I am a landscape photographer and I require a business card design. 

I require two designs:
1)  a double sided business card
 and
b)  a single sided business card 

The single sided design can either be the same as the double sided (with just one side having all the information)....or it can be an entire new design. Its up to you.

My corporate colours are (CMYK):

Blue   69, 32, 0, 0
Grey  72,  64,  47,  31
Green  32,  2,  91,  0
Yellow   0, 19, 92, 0
Orange  0, 39, 75, 0

Colour space in final file should be in CMYK.

The details that need to be included on the card:

- Use the provided Logo
- Name: Lukas Wendrovski
- Email:   sales@vistaplume.com.au
- Website:    vistaplume.com.au
- Twitter:    twitter.com/vistaplume
- Facebook:   facebook.com/vistaplume
- Mobile  0415 309 662

Please use the attached template to design the logo to the specified size, including the marked bleed lines. I have also attached my logo in PNG (transparent background) and ai format for you to use.

The final file should be:
- Photoshop version with layers so I can edit the name/text etc. All non vector files should be high resolution at 1039 x 697 pixels at 300 dpi.

I also require a file as:
- Vector based PDF

Anyway questions please contact me.

Thank you

Industry/Entity Type

Landscape

Logo styles of interest
Pictorial/Combination Logo
Abstract Logo
Wordmark Logo
Lettermark Logo
Requirements
Must have
• The details that need to be included on the card:

- Use the provided Logo
- Name: Lukas Wendrovski
- Email: sales@vistaplume.com.au
- Website: vistaplume.com.au
- Twitter: twitter.com/vistaplume
- Facebook: facebook.com/vistaplume
- Mobile 0415 309 662

```html
<!DOCTYPE html>
<html lang="en">
<head>
<meta charset="utf-8">
<title>Vista Plume – Business Cards</title>
<link rel="stylesheet" href="https://fonts.googleapis.com/css2?family=Cinzel:wght@500&family=Open+Sans:wght@300;400&display=swap">
<style>
  :root {
    --blue: #4a90d0;
    --grey: #474b58;
    --green: #b3cd44;
    --yellow: #fdcb2c;
    --orange: #f7a553;
    --card-grey: #8e9099;
    --paper: #ffffff;
    --stage: #3b3b3d;
  }
  * { box-sizing: border-box; margin: 0; padding: 0; }
  html, body { width: 1200px; height: 900px; overflow: hidden; }
  body {
    background: var(--stage);
    position: relative;
    font-family: "Open Sans", Arial, sans-serif;
  }
  .card { position: absolute; width: 525px; height: 345px; overflow: hidden; }
  .card--front { left: 58px; top: 105px; background: var(--card-grey); }
  .card--contact { left: 617px; top: 105px; background: var(--paper); }
  .card--single { left: 58px; top: 487px; height: 343px; background: var(--paper); }

  .brand { position: absolute; text-align: center; }
  .brand__dot { display: block; margin: 0 auto; border-radius: 50%; background: var(--grey); }
  .brand__name {
    display: block;
    font-family: "Cinzel", "Times New Roman", serif;
    font-weight: 500;
    color: var(--grey);
    white-space: nowrap;
  }

  /* Front */
  .card--front .brand { left: 0; right: 0; top: 108px; }
  .card--front .brand__dot { width: 62px; height: 62px; }
  .card--front .brand__name { font-size: 27px; margin-top: 36px; letter-spacing: 0.5px; }
  .front__web {
    position: absolute; left: 0; right: 0; top: 283px;
    text-align: center; font-size: 14px; font-weight: 300;
    letter-spacing: 2.6px; color: var(--grey);
  }
  .stripe { position: absolute; left: 0; right: 0; bottom: 0; height: 12px; display: flex; }
  .stripe span { flex: 1; }

  /* Contact side */
  .tree-art {
    position: absolute; left: 0; top: 0; width: 185px; height: 345px;
    background: linear-gradient(160deg, #b3cd44 0%, #4a90d0 35%, #474b58 55%, #fdcb2c 75%, #f7a553 100%);
    opacity: 0.85;
  }
  .card--contact .brand { left: 290px; width: 200px; top: 50px; }
  .card--contact .brand__dot { width: 48px; height: 48px; }
  .card--contact .brand__name { font-size: 19px; margin-top: 26px; }
  .ribbon {
    position: absolute; right: 0; height: 23px;
    clip-path: polygon(12px 0, 100% 0, 100% 100%, 0 100%, 6px 50%);
    text-align: right; padding-right: 40px;
    font-size: 12.5px; line-height: 23px; color: var(--paper);
  }
  .ribbon b, .row b { font-weight: 400; color: var(--grey); }

  /* Single side */
  .ghost-art {
    position: absolute; left: 0; top: 0; width: 232px; height: 190px;
    background: linear-gradient(135deg, #ececee 0%, #f3f3f3 60%, #f8f6ee 100%);
  }
  .card--single .brand { left: 0; right: 0; top: 40px; padding-left: 14px; }
  .card--single .brand__dot { width: 70px; height: 70px; }
  .card--single .brand__name { font-size: 25px; margin-top: 24px; }
  .row {
    position: absolute; left: 0; right: 0; height: 23px;
    background: var(--grey);
  }
  .row span {
    position: absolute; left: 26px; right: 26px; top: 0; bottom: 0;
    text-align: center; font-size: 12.5px; line-height: 23px; color: var(--paper);
  }
  .green { background: var(--green); }
  .orange { background: var(--orange); }
  .blue { background: var(--blue); }
  .yellow { background: var(--yellow); }
</style>
</head>
<body>

<section class="card card--front">
  <div class="brand">
    <span class="brand__dot"></span>
    <span class="brand__name">VISTA PLUME</span>
  </div>
  <p class="front__web">www.vistaplume.com.au</p>
  <div class="stripe">
    <span class="green"></span><span class="orange"></span><span class="blue"></span><span class="yellow"></span><span class="green"></span>
  </div>
</section>

<section class="card card--contact">
  <div class="tree-art" role="img" aria-label="Illustrated tree with colourful leaves"></div>
  <div class="brand">
    <span class="brand__dot"></span>
    <span class="brand__name">VISTA PLUME</span>
  </div>
  <p class="ribbon green" style="top:180px; left:308px;">mobile: <b>0415 309 662</b></p>
  <p class="ribbon orange" style="top:208px; left:236px;">email: <b>sales@vistaplume.com.au</b></p>
  <p class="ribbon blue" style="top:235px; left:228px;">website: <b>www.vistaplume.com.au</b></p>
  <p class="ribbon yellow" style="top:262px; left:280px;">twitter.com/<b>vistaplume</b></p>
  <p class="ribbon green" style="top:290px; left:263px;">facebook.com/<b>vistaplume</b></p>
</section>

<section class="card card--single">
  <div class="ghost-art" role="img" aria-label="Faint background decoration"></div>
  <div class="brand">
    <span class="brand__dot"></span>
    <span class="brand__name">VISTA PLUME</span>
  </div>
  <p class="row" style="top:189px;"><span class="green">mobile: <b>0415 309 662</b></span></p>
  <p class="row" style="top:216px;"><span class="orange">email: <b>sales@vistaplume.com.au</b></span></p>
  <p class="row" style="top:243px;"><span class="blue">website: <b>www.vistaplume.com.au</b></span></p>
  <p class="row" style="top:271px;"><span class="yellow">twitter.com/<b>vistaplume</b></span></p>
  <p class="row" style="top:298px;"><span class="green">facebook.com/<b>vistaplume</b></span></p>
</section>

</body>
</html>
```